DL Flyer and magnet design

I am in need of a new flyer design to show some offers on each side. First side Water filtration. Second side Heat pump hot water. I will attach an existing design from a previous flyer/magnet. I have also got some information to go on the flyer and images/logo.

Side 1: Water Filtration Solutions
Coral Ridge Pipeworks and Heating
Fresh, Clean Water for Every Tap

Water Filtration Solutions
1️⃣ High Flow Water Filtration
Starting from just $550!

2️⃣ Whole House Water Filtration
Enjoy pure water throughout your home – starting from $1800!

3️⃣ Whole House Water Filtration with UV Lamp (Perfect for rainwater systems)
Get the ultimate filtration – starting from $3000!

🎁 FREE BRAVO COOLER
With every water filtration system or referral!

📞 Call us today: 0491 837 254
🌐 Visit our website: www.coralridgeph.example.au

💧 Better water, better life. Call now for a free quote!

Side 2: Heat Pump Hot Water Systems
Energy-Efficient Hot Water Solutions

Heat Pump Hot Water Systems
🌟 Rebates Available!
Save big with government incentives on energy-efficient hot water systems.

💼 All Major Makes, Models, and Sizes
We supply and install trusted brands to suit your household’s needs.

💳 Interest-Free Finance Options
Upgrade now and pay later with flexible payment plans.

🎁 FREE BRAVO COOLER
With every heat pump system or referral!

💧 Upgrade to energy-efficient hot water and save!

Please include on the flyer. Valid until 30/6/2-25 Images are for illustrative purposes only and may not represent the exact product or service provided

```html
<!DOCTYPE html>
<html lang="en">
<head>
<meta charset="utf-8">
<title>Coral Ridge Pipeworks and Heating – DL Flyer</title>
<link href="https://fonts.googleapis.com/css2?family=Roboto+Condensed:wght@400;500;700&display=swap" rel="stylesheet">
<style>
  :root {
    --navy: #2b3390;
    --orange: #f47b20;
    --ink: #111111;
    --paper: #ffffff;
    --backdrop: #8a8a8a;
  }
  * { box-sizing: border-box; margin: 0; padding: 0; }
  html, body { width: 1200px; height: 1200px; overflow: hidden; }
  body {
    background: var(--backdrop);
    font-family: "Roboto Condensed", "Arial Narrow", sans-serif;
    position: relative;
  }
  .flyer {
    position: absolute;
    top: 71px;
    width: 497px;
    height: 1055px;
    background: var(--paper);
    overflow: hidden;
  }
  .flyer--filtration { left: 83px; }
  .flyer--heatpump { left: 620px; }
  .abs { position: absolute; }

  /* brand lockup */
  .brand { display: flex; align-items: center; gap: 12px; }
  .brand__mark { width: 56px; height: 56px; background: var(--navy); flex: none; }
  .brand__name {
    color: var(--navy); font-weight: 700; font-size: 27px; line-height: 1.05;
    text-transform: uppercase; letter-spacing: .3px;
  }

  /* filtration side */
  .f-brand { left: 30px; top: 70px; width: 440px; }
  .f-title { left: 30px; top: 194px; font-size: 47px; font-weight: 700; color: var(--ink); line-height: 1; }
  .f-title-accent { left: 30px; top: 240px; font-size: 72px; font-weight: 700; color: var(--orange); line-height: 1; }

  .offer { left: 0; width: 100%; color: #fff; }
  .offer__label { font-weight: 700; font-size: 19px; text-transform: uppercase; line-height: 1.25; }
  .offer__desc { font-size: 18px; line-height: 1.3; }
  .offer__price { position: absolute; right: 30px; font-size: 34px; font-weight: 700; }
  .offer--one { top: 364px; height: 102px; background: var(--navy); padding: 30px 0 0 30px; }
  .offer--one .offer__price { top: 30px; }
  .offer--two { top: 476px; height: 113px; background: var(--navy); }
  .offer--two .offer__text { position: absolute; left: 0; top: 0; width: 350px; height: 100%; background: var(--orange); padding: 22px 0 0 30px; }
  .offer--two .offer__price { top: 38px; right: 30px; }
  .offer--three { top: 600px; height: 145px; background: var(--navy); padding: 24px 0 0 30px; }
  .offer--three .offer__price { top: 22px; }

  .gift { left: 0; width: 100%; text-align: center; }
  .gift__title { font-size: 38px; font-weight: 700; line-height: 1; }
  .gift__note { font-size: 20px; margin-top: 6px; }
  .f-gift { top: 855px; top: 785px; }
  .f-gift .gift__title { color: var(--orange); }
  .f-gift .gift__note { color: var(--ink); }

  .contact { left: 0; width: 100%; text-align: center; font-size: 19px; }
  .contact__phone { font-size: 38px; font-weight: 700; font-style: italic; vertical-align: -3px; }
  .f-contact { top: 890px; color: var(--ink); }
  .f-contact .contact__phone { color: var(--navy); }
  .f-footer {
    left: 0; bottom: 0; width: 100%; height: 76px; background: var(--orange);
    color: #fff; font-size: 20px; display: flex; align-items: center; justify-content: center;
  }

  /* heat pump side */
  .h-title { left: 32px; top: 44px; font-size: 78px; font-weight: 700; color: var(--navy); line-height: 1; }
  .h-subtitle { left: 32px; top: 122px; font-size: 41px; font-weight: 700; color: var(--ink); line-height: 1; }
  .h-intro { left: 32px; top: 213px; font-size: 18px; font-weight: 700; color: var(--ink); line-height: 1.4; text-transform: uppercase; }
  .features { left: 0; top: 282px; width: 100%; height: 307px; background: var(--orange); color: #fff; padding: 20px 30px 0 32px; }
  .feature { margin-bottom: 17px; }
  .feature__title { font-size: 22px; font-weight: 700; text-transform: uppercase; line-height: 1.2; }
  .feature__desc { font-size: 18px; line-height: 1.35; }
  .h-gift { top: 622px; }
  .h-gift .gift__title { color: var(--navy); font-size: 42px; }
  .h-gift .gift__note { color: var(--ink); }
  .h-contact {
    top: 721px; height: 148px; background: var(--navy); color: #fff;
    padding-top: 18px; line-height: 1.45;
  }
  .h-contact .contact__tagline { margin-top: 14px; }
  .h-brand { left: 40px; top: 908px; width: 430px; }
  .h-valid { right: 40px; top: 1000px; font-size: 17px; color: var(--ink); }
</style>
</head>
<body>

<section class="flyer flyer--filtration">
  <div class="abs brand f-brand">
    <span class="brand__mark"></span>
    <span class="brand__name">Coral Ridge Pipeworks<br>and Heating</span>
  </div>
  <h1 class="abs f-title">WATER FILTRATION</h1>
  <h2 class="abs f-title-accent">SOLUTIONS</h2>

  <div class="abs offer offer--one">
    <p class="offer__label">High Flow Water Filtration</p>
    <p class="offer__desc">Starting from just</p>
    <span class="offer__price">$550!</span>
  </div>
  <div class="abs offer offer--two">
    <div class="offer__text">
      <p class="offer__label">Whole House Water Filtration</p>
      <p class="offer__desc">Enjoy pure water throughout your home<br>– starting from</p>
    </div>
    <span class="offer__price">$1800!</span>
  </div>
  <div class="abs offer offer--three">
    <p class="offer__label">Whole House Water Filtration<br>with UV Lamp</p>
    <p class="offer__desc">(Perfect for rainwater systems)<br>Get the ultimate filtration – starting from</p>
    <span class="offer__price">$3000!</span>
  </div>

  <div class="abs gift f-gift">
    <p class="gift__title">FREE BRAVO COOLER</p>
    <p class="gift__note">With every water filtration system or referral!</p>
  </div>
  <div class="abs contact f-contact">
    <p>Call us today: <span class="contact__phone">0491 837 254</span></p>
    <p>Visit our website: www.coralridgeph.example.au</p>
  </div>
  <div class="abs f-footer">Better water, better life. Call now for a free quote!</div>
</section>

<section class="flyer flyer--heatpump">
  <h1 class="abs h-title">HEAT PUMP</h1>
  <h2 class="abs h-subtitle">HOT WATER SYSTEMS</h2>
  <p class="abs h-intro">Coral Ridge Pipeworks and Heating<br>Energy-efficient hot water solutions</p>

  <div class="abs features">
    <div class="feature">
      <p class="feature__title">Rebates Available!</p>
      <p class="feature__desc">Save big with government incentives on energy-efficient hot water systems.</p>
    </div>
    <div class="feature">
      <p class="feature__title">All Major Makes, Models, and Sizes</p>
      <p class="feature__desc">We supply and install trusted brands to suit your household's needs.</p>
    </div>
    <div class="feature">
      <p class="feature__title">Interest-Free Finance Options</p>
      <p class="feature__desc">Upgrade now and pay later with flexible payment plans.</p>
    </div>
  </div>

  <div class="abs gift h-gift">
    <p class="gift__title">FREE BRAVO COOLER</p>
    <p class="gift__note">With every heat pump system or referral!</p>
  </div>
  <div class="abs contact h-contact">
    <p>Call us today: <span class="contact__phone">0491 837 254</span></p>
    <p>Visit our website: www.coralridgeph.example.au</p>
    <p class="contact__tagline">Upgrade to energy-efficient hot water and save!</p>
  </div>

  <div class="abs brand h-brand">
    <span class="brand__mark"></span>
    <span class="brand__name">Coral Ridge Pipeworks<br>and Heating</span>
  </div>
  <p class="abs h-valid">*Valid until 30-06-2025</p>
</section>

</body>
</html>
```